Visitenkarten-Design für italienisches Küchenschiff
Zielgruppe
Restaurantschiff Morvella
Aufgabenstellung
Wir sind ein italienische Küche Schiff auf der Binnenalster in Hamburg und wollen den schönen Blick und gerne auch die italienischen Farben widerspiegeln...ich brauche das einmal neutral für den normalen Gast....und würde das denn..wenn es denn gut wird...auch gerne individell mit m e i n e r Tel Nr und auch für meine führenden Mitarbeiter personalisieren...aber...zuerst natürlich das neutrale...dazu schicke ich die alte Karte mit dem auch alten Logo was nicht unbedingt verwendet werden muss...

```html
<!DOCTYPE html>
<html lang="de">
<head>
<meta charset="utf-8">
<title>Morvella Visitenkarten</title>
<link rel="stylesheet" href="https://fonts.googleapis.com/css2?family=Advent+Pro:wght@300&display=swap">
<style>
  :root {
    --stage: #4a4a4a;
    --card-warm: #4a4746;
    --card-dark: #393939;
    --ink: #8c7e6c;
    --green: #009a57;
    --white: #ffffff;
    --red: #ac3434;
    --photo-day-a: #8fa6b8;
    --photo-day-b: #a23a3a;
    --photo-night-a: #8e7584;
    --photo-night-b: #2d2a33;
  }
  * { margin: 0; padding: 0; box-sizing: border-box; }
  html, body { width: 1200px; height: 1200px; overflow: hidden; background: var(--stage); }
  body { position: relative; font-family: "Advent Pro", sans-serif; font-weight: 300; color: var(--ink); }

  .card { position: absolute; width: 510px; height: 329px; box-shadow: 3px 4px 6px rgba(0,0,0,.45); }
  .card--warm { background: var(--card-warm); }
  .card--dark { background: var(--card-dark); }
  .card .t { position: absolute; white-space: nowrap; line-height: 1; }

  /* front */
  .flag-strip { position: absolute; left: 0; top: 0; width: 14px; height: 100%; display: flex; flex-direction: column; }
  .flag-strip span { flex: 1; }
  .green { background: var(--green); } .white { background: var(--white); } .red { background: var(--red); }
  .portrait { position: absolute; left: 89px; top: 45px; width: 99px; height: 124px;
    background: linear-gradient(180deg, #9a8a70 0%, #6d6458 35%, #1f2a3a 60%, #1b2433 100%); }
  .person { left: 78px; width: 120px; text-align: center; font-size: 17px; }
  .contact-label { font-size: 17px; }
  .divider { position: absolute; left: 259px; top: 29px; width: 1px; height: 280px; background: var(--ink); opacity: .7; }
  .brand { left: 278px; top: 94px; font-size: 36px; letter-spacing: 1px; }
  .brand-dot { position: absolute; left: 440px; top: 104px; width: 18px; height: 18px; border-radius: 50%; background: var(--ink); }
  .tagline { left: 278px; top: 126px; font-size: 15px; letter-spacing: 4.6px; }
  .info { left: 278px; font-size: 16px; }

  /* back */
  .photo { position: absolute; left: 22px; width: 211px; }
  .photo--day { top: 20px; height: 128px;
    background: linear-gradient(180deg, #a26b3a 0%, #7e9cb5 18%, #5f7f8c 45%, var(--photo-day-b) 72%, #e8e4de 88%); }
  .photo--night { top: 163px; height: 125px;
    background: linear-gradient(180deg, var(--photo-night-a) 0%, #5a4b5a 55%, #6f6a5a 72%, var(--photo-night-b) 100%); }
  .heading { left: 257px; font-size: 21px; }
  .body-text { left: 257px; font-size: 16.5px; }
  .kitchen { right: 27px; font-size: 16.5px; }
  .rule { position: absolute; left: 309px; top: 155px; width: 122px; height: 1px; background: var(--ink); }
  .flag-band { position: absolute; left: 0; top: 300px; width: 100%; height: 9px; display: flex; }
  .flag-band span { flex: 1; }
</style>
</head>
<body>

<!-- front, warm -->
<section class="card card--warm" style="left:61px; top:160px;">
  <div class="flag-strip"><span class="green"></span><span class="white"></span><span class="red"></span></div>
  <div class="portrait" role="img" aria-label="Portraitfoto des Gastgebers an Bord"></div>
  <div class="t person" style="top:176px;">Lorenz Halberg</div>
  <div class="t person" style="top:198px;">Capo</div>
  <div class="t contact-label" style="left:42px; top:264px;">Tel:&nbsp;&nbsp;&nbsp;&nbsp;&nbsp;&nbsp;&nbsp;+49 171 604 2819</div>
  <div class="t contact-label" style="left:42px; top:286px;">E-Mail:&nbsp;&nbsp;kalorix7@postfeld.de</div>
  <div class="divider"></div>
  <div class="t brand">MORVELLA</div>
  <div class="brand-dot"></div>
  <div class="t tagline">Schiffsrestaurant</div>
  <div class="t info" style="top:162px;">Uferweg 7b (Wasserseite)</div>
  <div class="t info" style="top:181px;">20095 Hamburg</div>
  <div class="t info" style="top:206px;">Kontakt</div>
  <div class="t info" style="top:227px;">Tel:&nbsp;&nbsp;&nbsp;+49 040 / 55 18 40</div>
  <div class="t info" style="top:247px;">Fax:&nbsp;&nbsp;+49 040 / 55 18 41</div>
  <div class="t info" style="top:266px; letter-spacing:.6px;">www.alsterschiff-morvella.de</div>
  <div class="t info" style="top:287px;">E-Mail: info@alsterschiff-morvella.de</div>
</section>

<!-- back, warm -->
<section class="card card--warm" style="left:628px; top:161px;">
  <div class="photo photo--day" role="img" aria-label="Blick aus dem Schiffsinneren mit gedeckten Tischen auf die Binnenalster"></div>
  <div class="photo photo--night" role="img" aria-label="Nächtliche Uferpromenade der Binnenalster mit Lichtern im Wasser"></div>
  <div class="t heading" style="top:47px;">Öffnungszeiten</div>
  <div class="t body-text" style="top:73px;">Montag - Sonntag&nbsp;&nbsp;&nbsp;&nbsp;&nbsp;12:00 - 23:00</div>
  <div class="t kitchen" style="top:99px;">Küche bis 22:00</div>
  <div class="rule"></div>
  <div class="t heading" style="top:180px;">Reservierungen</div>
  <div class="t body-text" style="top:206px;">Wir freuen uns auf Ihren Anruf oder</div>
  <div class="t body-text" style="top:228px;">eine E-Mail:</div>
  <div class="t body-text" style="top:249px;">reservierung@alsterschiff-morvella.de</div>
  <div class="flag-band"><span class="green"></span><span class="white"></span><span class="red"></span></div>
</section>

<!-- front, dark -->
<section class="card card--dark" style="left:61px; top:607px;">
  <div class="flag-strip"><span class="green"></span><span class="white"></span><span class="red"></span></div>
  <div class="portrait" role="img" aria-label="Portraitfoto des Gastgebers an Bord"></div>
  <div class="t person" style="top:176px;">Lorenz Halberg</div>
  <div class="t person" style="top:198px;">Capo</div>
  <div class="t contact-label" style="left:42px; top:264px;">Tel:&nbsp;&nbsp;&nbsp;&nbsp;&nbsp;&nbsp;&nbsp;+49 171 604 2819</div>
  <div class="t contact-label" style="left:42px; top:286px;">E-Mail:&nbsp;&nbsp;kalorix7@postfeld.de</div>
  <div class="divider"></div>
  <div class="t brand">MORVELLA</div>
  <div class="brand-dot"></div>
  <div class="t tagline">Schiffsrestaurant</div>
  <div class="t info" style="top:162px;">Uferweg 7b (Wasserseite)</div>
  <div class="t info" style="top:181px;">20095 Hamburg</div>
  <div class="t info" style="top:206px;">Kontakt</div>
  <div class="t info" style="top:227px;">Tel:&nbsp;&nbsp;&nbsp;+49 040 / 55 18 40</div>
  <div class="t info" style="top:247px;">Fax:&nbsp;&nbsp;+49 040 / 55 18 41</div>
  <div class="t info" style="top:266px; letter-spacing:.6px;">www.alsterschiff-morvella.de</div>
  <div class="t info" style="top:287px;">E-Mail: info@alsterschiff-morvella.de</div>
</section>

<!-- back, dark -->
<section class="card card--dark" style="left:628px; top:608px;">
  <div class="photo photo--day" role="img" aria-label="Blick aus dem Schiffsinneren mit gedeckten Tischen auf die Binnenalster"></div>
  <div class="photo photo--night" role="img" aria-label="Nächtliche Uferpromenade der Binnenalster mit Lichtern im Wasser"></div>
  <div class="t heading" style="top:47px;">Öffnungszeiten</div>
  <div class="t body-text" style="top:73px;">Montag - Sonntag&nbsp;&nbsp;&nbsp;&nbsp;&nbsp;12:00 - 23:00</div>
  <div class="t kitchen" style="top:99px;">Küche bis 22:00</div>
  <div class="rule"></div>
  <div class="t heading" style="top:180px;">Reservierungen</div>
  <div class="t body-text" style="top:206px;">Wir freuen uns auf Ihren Anruf oder</div>
  <div class="t body-text" style="top:228px;">eine E-Mail:</div>
  <div class="t body-text" style="top:249px;">reservierung@alsterschiff-morvella.de</div>
  <div class="flag-band"><span class="green"></span><span class="white"></span><span class="red"></span></div>
</section>

</body>
</html>
```